Virtual Assistant/Online Marketing Business Card/Stationary

I need a professional but modern business card/stationary for my company in Dallas called BrivoLane. BrivoLane is a virtual assistant specializing in online marketing. I would like a unique design that stands out and makes my brand clear. Incorporating the logo is a must and have attached it to this brief.

Target Market(s)

small business owners & entrepreneurs, 35-65

Industry/Entity Type

Business

Contact Information for Business Card

Dorla Finch
dorlafinch@brivolane.biz
(214) 555-0187
brivolane.biz

Font styles to use
Sans Serif

Colors
f04a50
3176b5
9bcb3c

Requirements
Must have
• Colors that match the logo colors. Logo integration

```html
<!DOCTYPE html>
<html lang="en">
<head>
<meta charset="utf-8">
<title>BrivoLane Business Card</title>
<link rel="stylesheet" href="https://fonts.googleapis.com/css2?family=Open+Sans:wght@400;700&display=swap">
<style>
  :root {
    --brand-red: #f04a50;
    --brand-red-deep: #c8202a;
    --brand-blue: #3176b5;
    --brand-green: #9bcb3c;
    --brand-green-deep: #5f9e35;
    --ink: #2e2f31;
    --card-face: #f6f7f8;
    --backdrop: #e6e6e4;
  }
  * { margin: 0; padding: 0; box-sizing: border-box; }
  html, body {
    width: 1200px;
    height: 970px;
    overflow: hidden;
    background: var(--backdrop);
    font-family: "Open Sans", Arial, sans-serif;
  }
  .business-card {
    position: absolute;
    left: 80px;
    top: 190px;
    width: 1040px;
    height: 590px;
    border-radius: 18px;
    overflow: hidden;
    background: var(--card-face);
    box-shadow: 0 10px 30px rgba(0,0,0,0.18);
  }
  .accent-area {
    position: absolute;
    right: 0;
    top: 0;
    width: 235px;
    height: 590px;
    background: linear-gradient(180deg, var(--brand-green) 0%, var(--brand-green-deep) 70%, var(--brand-red-deep) 100%);
  }
  .accent-band {
    position: absolute;
    left: 0;
    bottom: 0;
    width: 805px;
    height: 44px;
    background: linear-gradient(90deg, var(--brand-red) 0%, var(--brand-red-deep) 100%);
  }
  .brand {
    position: absolute;
    left: 74px;
    top: 180px;
    display: flex;
    align-items: center;
    gap: 16px;
  }
  .brand-mark {
    width: 30px;
    height: 30px;
    background: var(--brand-red);
  }
  .brand-name {
    font-size: 74px;
    font-weight: 700;
    color: var(--ink);
    letter-spacing: -1px;
    line-height: 1;
  }
  .holder-name {
    position: absolute;
    left: 74px;
    top: 350px;
    font-size: 33px;
    font-weight: 700;
    color: var(--ink);
    letter-spacing: 0.5px;
  }
  .contact-list {
    position: absolute;
    left: 74px;
    top: 405px;
    list-style: none;
    font-size: 29px;
    color: var(--ink);
    line-height: 36px;
  }
  .contact-item {
    display: flex;
    align-items: center;
    gap: 14px;
  }
  .contact-icon {
    width: 28px;
    height: 28px;
    border-radius: 4px;
    background: var(--brand-blue);
    display: flex;
    align-items: center;
    justify-content: center;
  }
</style>
</head>
<body>
  <div class="business-card">
    <div class="accent-area" role="img" aria-label="Decorative green and red brand accent area"></div>
    <div class="accent-band" role="img" aria-label="Decorative red brand accent band"></div>

    <div class="brand">
      <span class="brand-name">BrivoLane</span>
      <span class="brand-mark"></span>
    </div>

    <h1 class="holder-name">DORLA FINCH</h1>

    <ul class="contact-list">
      <li class="contact-item">
        <span class="contact-icon">
          <svg width="18" height="18" viewBox="0 0 24 24"><path fill="#fff" d="M6.6 10.8a15.1 15.1 0 0 0 6.6 6.6l2.2-2.2a1 1 0 0 1 1-.25 11.4 11.4 0 0 0 3.6.57 1 1 0 0 1 1 1V20a1 1 0 0 1-1 1A17 17 0 0 1 3 4a1 1 0 0 1 1-1h3.5a1 1 0 0 1 1 1c0 1.25.2 2.450.57 3.6a1 1 0 0 1-.25 1Z"/></svg>
        </span>
        <span class="contact-text">(214) 555-0187</span>
      </li>
      <li class="contact-item">
        <span class="contact-icon">
          <svg width="18" height="14" viewBox="0 0 18 14"><rect x="1" y="1" width="16" height="12" fill="none" stroke="#fff" stroke-width="1.6"/><path d="M1 1 L9 8 L17 1" fill="none" stroke="#fff" stroke-width="1.6"/></svg>
        </span>
        <span class="contact-text">dorlafinch@brivolane.biz</span>
      </li>
      <li class="contact-item">
        <span class="contact-text">brivolane.biz</span>
      </li>
    </ul>
  </div>
</body>
</html>
```